female esthetician looking for an impact business card

I an an expert in skin care industry with high experience in NYC.I want my business card to look professional , an impact at first look. I do want a combination between white and gold . I believe the font will be great if is gold.. The Fonts are also important. MARISELA VONDRAKE (SKIN CARE BOUTIQUE)

THIS SHOULD BE THE BUSINESS NAME, and should be placed on th eback of the card.
IN front m, the name MARISELA VONDRAKE - ESTHETCIAN

BY APPOINTMENTS ONLY: 555.218.9031

Target Market(s)

HIGH END CLIENTELE

Contact Information for Business Card

iT WILL BE on a luxury paper. I neeed the wow feeling

Requirements
Should not have
• pictures

```html
<!DOCTYPE html>
<html lang="en">
<head>
<meta charset="utf-8">
<title>Marisela Vondrake Skin Care Boutique Business Card</title>
<link href="https://fonts.googleapis.com/css2?family=Lato:wght@400;700&family=Roboto+Slab:wght@400;500&display=swap" rel="stylesheet">
<style>
  :root {
    --backdrop: #7a4826;
    --card: #222021;
    --gold: #fcc03a;
    --gold-name: #f6d23f;
    --white: #f7f4ee;
  }
  * { margin: 0; padding: 0; box-sizing: border-box; }
  html, body { width: 1200px; height: 900px; overflow: hidden; }
  body { background: var(--backdrop); position: relative; font-family: "Lato", sans-serif; }

  .card {
    position: absolute;
    background: var(--card);
    box-shadow: 4px 6px 10px rgba(0,0,0,0.45);
    overflow: hidden;
  }
  .card-front { left: 330px; top: 90px; width: 555px; height: 344px; }
  .card-back  { left: 330px; top: 470px; width: 559px; height: 343px; }

  .gold-band {
    position: absolute; left: 0; right: 0; bottom: 0; height: 10px;
    background: var(--gold);
  }

  .brand-mark {
    position: absolute; border-radius: 50%; background: var(--gold);
  }
  .card-front .brand-mark { left: 118px; top: 34px; width: 42px; height: 42px; }
  .card-back .brand-mark  { left: 255px; top: 84px; width: 48px; height: 48px; }

  .brand-name {
    position: absolute; font-family: "Roboto Slab", serif; font-weight: 500;
    color: var(--gold-name); text-align: center; white-space: nowrap;
    letter-spacing: 0.5px;
  }
  .brand-tagline {
    position: absolute; font-family: "Roboto Slab", serif; font-weight: 400;
    color: var(--white); text-align: center; white-space: nowrap;
  }
  .card-front .brand-name    { left: 0; width: 280px; top: 142px; font-size: 21px; line-height: 28px; }
  .card-front .brand-tagline { left: 0; width: 280px; top: 172px; font-size: 16px; line-height: 20px; }
  .card-back .brand-name     { left: 0; width: 559px; top: 204px; font-size: 25px; line-height: 32px; }
  .card-back .brand-tagline  { left: 0; width: 559px; top: 238px; font-size: 18px; line-height: 22px; }

  .person {
    position: absolute; right: 29px; top: 48px; text-align: right;
  }
  .person-name { color: var(--gold); font-weight: 700; font-size: 22px; line-height: 26px; }
  .person-role { color: var(--white); font-size: 16px; line-height: 18px; }

  .contact-list {
    position: absolute; left: 25px; top: 250px; list-style: none;
    color: var(--white); font-size: 16px; line-height: 20.5px;
  }
  .contact-list li { display: flex; align-items: center; gap: 5px; }
  .contact-icon { width: 13px; height: 13px; fill: var(--gold); flex: none; }

  .address {
    position: absolute; right: 29px; top: 269px; text-align: right;
    color: var(--white); font-size: 16px; line-height: 20.5px;
  }
</style>
</head>
<body>

  <section class="card card-front">
    <span class="brand-mark"></span>
    <p class="brand-name">MARISELA VONDRAKE</p>
    <p class="brand-tagline">skin care boutique</p>

    <div class="person">
      <p class="person-name">MARISELA VONDRAKE</p>
      <p class="person-role">Esthetician</p>
    </div>

    <ul class="contact-list">
      <li>
        <svg class="contact-icon" viewBox="0 0 16 16"><path d="M2 6c0-2 2-3 6-3s6 1 6 3v1h-3V6H5v1H2z M4 8h8l2 5H2z"/></svg>
        555.218.9031
      </li>
      <li>
        <svg class="contact-icon" viewBox="0 0 16 16"><path d="M1 3h14v10H1z"/><path d="M1 3l7 6 7-6" fill="none" stroke="#222021" stroke-width="1.5"/></svg>
        hello@vondrakeskin.com
      </li>
      <li>
        <svg class="contact-icon" viewBox="0 0 16 16"><circle cx="8" cy="8" r="7"/><path d="M1 8h14M8 1c-3 4-3 10 0 14M8 1c3 4 3 10 0 14" fill="none" stroke="#222021" stroke-width="1.2"/></svg>
        www.vondrakeskin.com
      </li>
    </ul>

    <div class="address">
      <p>88, Mercer Street</p>
      <p>New York, NY 10012</p>
    </div>

    <div class="gold-band"></div>
  </section>

  <section class="card card-back">
    <span class="brand-mark"></span>
    <p class="brand-name">MARISELA VONDRAKE</p>
    <p class="brand-tagline">skin care boutique</p>
    <div class="gold-band"></div>
  </section>

</body>
</html>
```